Memento Mori Calendar

I’m looking for a graphic designer to create a Memento Mori–style life calendar that captures the essence of OLVENTRA — minimal, timeless, and deeply philosophical.

The design should be black and white only, with a refined, clean aesthetic and a sense of stillness and precision.
It should feel modern yet eternal, reflecting the themes of time, mortality, and presence.

Deliverables (Print-Ready Files):

24 x 30 in

24 x 32 in

24 x 36 in

A1 (594 x 841 mm)

All formats should be high-resolution and ready for professional printing (300 DPI, CMYK).

Design Requirements:

The calendar layout should follow the Memento Mori life calendar concept (weeks of life represented as small squares or circles).

The overall tone: minimal, meditative, monochrome.

Include the brand name: OLVENTRA (in an elegant, understated placement).

Add the following quote at the bottom or in a subtle position:

“Life can only be understood backwards; but it must be lived forwards.”
— Henrik Vastmoe

Target Market(s)

The OLVENTRA audience consists of urban, creative individuals aged 25 to 45, belonging to a middle to upper-middle income class. They lead conscious, quietly ambitious lives, seeking balance between inner depth and modern design. Their values center on awareness, presence, authenticity, and emotional depth, reflected in their preference for a monochrome, minimal, and timeless aesthetic. They tend to be introverted, reflective, and spiritually curious, drawn to brands that embody meaning and restraint rather than excess. Their cultural and stylistic affinities include Pyrel, Tulve, Ni Ostra, The Quiet Bench Guild, Durvanne, and Ombrix — labels that share OLVENTRAs devotion to simplicity, substance, and subtle ritual.

Font styles to use
Serif
Sans Serif

Colors

Designer to choose only greyscale colors for use in the design.

Requirements
Must have
• The calendar layout should follow the Memento Mori life calendar concept (weeks of life represented as small squares or circles). The overall tone: minimal, meditative, monochrome. Include the brand name: qrnvalto (in an elegant, understated placement). Add the following quote at the bottom or in a subtle position: “Life can only be understood backwards; but it must be lived forwards.” — Henrik Vastmoe

```html
<!DOCTYPE html>
<html lang="en">
<head>
<meta charset="utf-8">
<title>Memento Mori — OLVENTRA</title>
<link rel="stylesheet" href="https://fonts.googleapis.com/css2?family=Jost:wght@400;500;600;700&display=swap">
<style>
  :root {
    --paper: #ffffff;
    --ink: #000000;
    --ink-soft: #222222;
  }
  html, body {
    margin: 0;
    padding: 0;
    width: 940px;
    height: 1200px;
    overflow: hidden;
    background: var(--paper);
  }
  .poster {
    display: block;
    width: 940px;
    height: 1200px;
    font-family: "Jost", sans-serif;
  }
  .title { font-weight: 700; font-size: 60px; fill: var(--ink); }
  .axis-title { font-weight: 500; font-size: 13px; fill: var(--ink); }
  .week-num { font-size: 5px; fill: var(--ink-soft); text-anchor: middle; }
  .week-num--major { font-size: 9.5px; font-weight: 600; fill: var(--ink); }
  .year-num { font-size: 5.5px; fill: var(--ink-soft); }
  .year-num--major { font-size: 10px; fill: var(--ink); }
  .week-box { fill: none; stroke: var(--ink); stroke-width: 0.7; }
  .milestone-dot { fill: var(--ink); }
  .quote { font-size: 16px; fill: var(--ink); text-anchor: middle; }
  .quote-author { font-size: 10.5px; font-weight: 700; letter-spacing: 0.8px; fill: var(--ink); text-anchor: middle; }
  .brand-band { fill: var(--ink); }
  .brand-name { font-size: 15px; font-weight: 500; fill: var(--paper); letter-spacing: 0.3px; }
</style>
</head>
<body>
<svg class="poster" viewBox="0 0 940 1200" xmlns="http://www.w3.org/2000/svg" role="img" aria-label="Memento Mori life calendar: 80 years of 52 weeks">
  <defs>
    <g id="week-row" transform="translate(0.4 0.4)">
      <rect class="week-box" x="0" y="0" width="6.6" height="6.6"/>
      <rect class="week-box" x="14.07" y="0" width="6.6" height="6.6"/>
      <rect class="week-box" x="28.14" y="0" width="6.6" height="6.6"/>
      <rect class="week-box" x="42.21" y="0" width="6.6" height="6.6"/>
      <rect class="week-box" x="56.28" y="0" width="6.6" height="6.6"/>
      <rect class="week-box" x="70.35" y="0" width="6.6" height="6.6"/>
      <rect class="week-box" x="84.42" y="0" width="6.6" height="6.6"/>
      <rect class="week-box" x="98.49" y="0" width="6.6" height="6.6"/>
      <rect class="week-box" x="112.56" y="0" width="6.6" height="6.6"/>
      <rect class="week-box" x="126.63" y="0" width="6.6" height="6.6"/>
      <rect class="week-box" x="140.7" y="0" width="6.6" height="6.6"/>
      <rect class="week-box" x="154.77" y="0" width="6.6" height="6.6"/>
      <rect class="week-box" x="168.84" y="0" width="6.6" height="6.6"/>
      <rect class="week-box" x="182.91" y="0" width="6.6" height="6.6"/>
      <rect class="week-box" x="196.98" y="0" width="6.6" height="6.6"/>
      <rect class="week-box" x="211.05" y="0" width="6.6" height="6.6"/>
      <rect class="week-box" x="225.12" y="0" width="6.6" height="6.6"/>
      <rect class="week-box" x="239.19" y="0" width="6.6" height="6.6"/>
      <rect class="week-box" x="253.26" y="0" width="6.6" height="6.6"/>
      <rect class="week-box" x="267.33" y="0" width="6.6" height="6.6"/>
      <rect class="week-box" x="281.4" y="0" width="6.6" height="6.6"/>
      <rect class="week-box" x="295.47" y="0" width="6.6" height="6.6"/>
      <rect class="week-box" x="309.54" y="0" width="6.6" height="6.6"/>
      <rect class="week-box" x="323.61" y="0" width="6.6" height="6.6"/>
      <rect class="week-box" x="337.68" y="0" width="6.6" height="6.6"/>
      <rect class="week-box" x="351.75" y="0" width="6.6" height="6.6"/>
    </g>
    <g id="half-decade">
      <use href="#week-row" y="0"/>
      <use href="#week-row" y="10.52"/>
      <use href="#week-row" y="21.04"/>
      <use href="#week-row" y="31.56"/>
      <use href="#week-row" y="42.08"/>
      <use href="#week-row" y="52.6"/>
      <use href="#week-row" y="63.12"/>
      <use href="#week-row" y="73.64"/>
      <use href="#week-row" y="84.16"/>
      <use href="#week-row" y="94.68"/>
    </g>
    <g id="decade-block">
      <use href="#half-decade" x="101.6" y="145.8"/>
      <use href="#half-decade" x="479.5" y="145.8"/>
    </g>
    <g id="milestone-row">
      <circle class="milestone-dot" cx="161.6" cy="257" r="1.2"/>
      <circle class="milestone-dot" cx="231.9" cy="257" r="1.2"/>
      <circle class="milestone-dot" cx="302.3" cy="257" r="1.2"/>
      <circle class="milestone-dot" cx="372.6" cy="257" r="1.2"/>
      <circle class="milestone-dot" cx="443.0" cy="257" r="1.2"/>
      <circle class="milestone-dot" cx="525.5" cy="257" r="1.2"/>
      <circle class="milestone-dot" cx="595.8" cy="257" r="1.2"/>
      <circle class="milestone-dot" cx="666.2" cy="257" r="1.2"/>
      <circle class="milestone-dot" cx="736.5" cy="257" r="1.2"/>
      <circle class="milestone-dot" cx="806.9" cy="257" r="1.2"/>
    </g>
  </defs>

  <rect width="940" height="1200" fill="var(--paper)"/>

  <text class="title" x="470" y="93" text-anchor="middle" textLength="477" lengthAdjust="spacingAndGlyphs">MEMENTO MORI</text>

  <text class="axis-title" x="102" y="119">WEEK</text>

  <g class="week-axis">
    <text class="week-num" x="105.3" y="138">1</text>
    <text class="week-num" x="119.4" y="138">2</text>
    <text class="week-num" x="133.4" y="138">3</text>
    <text class="week-num" x="147.5" y="138">4</text>
    <text class="week-num week-num--major" x="161.6" y="138">5</text>
    <text class="week-num" x="175.7" y="138">6</text>
    <text class="week-num" x="189.7" y="138">7</text>
    <text class="week-num" x="203.8" y="138">8</text>
    <text class="week-num" x="217.9" y="138">9</text>
    <text class="week-num week-num--major" x="231.9" y="138">10</text>
    <text class="week-num" x="246.0" y="138">11</text>
    <text class="week-num" x="260.1" y="138">12</text>
    <text class="week-num" x="274.1" y="138">13</text>
    <text class="week-num" x="288.2" y="138">14</text>
    <text class="week-num week-num--major" x="302.3" y="138">15</text>
    <text class="week-num" x="316.4" y="138">16</text>
    <text class="week-num" x="330.4" y="138">17</text>
    <text class="week-num" x="344.5" y="138">18</text>
    <text class="week-num" x="358.6" y="138">19</text>
    <text class="week-num week-num--major" x="372.6" y="138">20</text>
    <text class="week-num" x="386.7" y="138">21</text>
    <text class="week-num" x="400.8" y="138">22</text>
    <text class="week-num" x="414.8" y="138">23</text>
    <text class="week-num" x="428.9" y="138">24</text>
    <text class="week-num week-num--major" x="443.0" y="138">25</text>
    <text class="week-num" x="457.1" y="138">26</text>
    <text class="week-num" x="483.2" y="138">27</text>
    <text class="week-num" x="497.3" y="138">28</text>
    <text class="week-num" x="511.3" y="138">29</text>
    <text class="week-num week-num--major" x="525.4" y="138">30</text>
    <text class="week-num" x="539.5" y="138">31</text>
    <text class="week-num" x="553.6" y="138">32</text>
    <text class="week-num" x="567.6" y="138">33</text>
    <text class="week-num" x="581.7" y="138">34</text>
    <text class="week-num week-num--major" x="595.8" y="138">35</text>
    <text class="week-num" x="609.8" y="138">36</text>
    <text class="week-num" x="623.9" y="138">37</text>
    <text class="week-num" x="638.0" y="138">38</text>
    <text class="week-num" x="652.0" y="138">39</text>
    <text class="week-num week-num--major" x="666.1" y="138">40</text>
    <text class="week-num" x="680.2" y="138">41</text>
    <text class="week-num" x="694.3" y="138">42</text>
    <text class="week-num" x="708.3" y="138">43</text>
    <text class="week-num" x="722.4" y="138">44</text>
    <text class="week-num week-num--major" x="736.5" y="138">45</text>
    <text class="week-num" x="750.5" y="138">46</text>
    <text class="week-num" x="764.6" y="138">47</text>
    <text class="week-num" x="778.7" y="138">48</text>
    <text class="week-num" x="792.8" y="138">49</text>
    <text class="week-num week-num--major" x="806.8" y="138">50</text>
    <text class="week-num" x="820.9" y="138">51</text>
    <text class="week-num" x="835.0" y="138">52</text>
  </g>

  <g class="life-grid">
    <use href="#decade-block"/>
    <use href="#decade-block" y="120.8"/>
    <use href="#decade-block" y="241.6"/>
    <use href="#decade-block" y="362.4"/>
    <use href="#decade-block" y="483.2"/>
    <use href="#decade-block" y="604"/>
    <use href="#decade-block" y="724.8"/>
    <use href="#decade-block" y="845.6"/>
  </g>

  <g class="milestones">
    <use href="#milestone-row"/>
    <use href="#milestone-row" y="120.8"/>
    <use href="#milestone-row" y="241.6"/>
    <use href="#milestone-row" y="362.4"/>
    <use href="#milestone-row" y="483.2"/>
    <use href="#milestone-row" y="604"/>
    <use href="#milestone-row" y="724.8"/>
  </g>

  <g class="year-axis">
    <g>
      <text class="year-num" x="846" y="152">1</text><text class="year-num" x="846" y="162.5">2</text><text class="year-num" x="846" y="173">3</text><text class="year-num" x="846" y="183.6">4</text><text class="year-num" x="846" y="194.1">5</text><text class="year-num" x="846" y="204.6">6</text><text class="year-num" x="846" y="215.1">7</text><text class="year-num" x="846" y="225.7">8</text><text class="year-num" x="846" y="236.2">9</text><text class="year-num year-num--major" x="846" y="249">10</text>
    </g>
    <g transform="translate(0 120.8)">
      <text class="year-num" x="846" y="152">11</text><text class="year-num" x="846" y="162.5">12</text><text class="year-num" x="846" y="173">13</text><text class="year-num" x="846" y="183.6">14</text><text class="year-num" x="846" y="194.1">15</text><text class="year-num" x="846" y="204.6">16</text><text class="year-num" x="846" y="215.1">17</text><text class="year-num" x="846" y="225.7">18</text><text class="year-num" x="846" y="236.2">19</text><text class="year-num year-num--major" x="846" y="249">20</text>
    </g>
    <g transform="translate(0 241.6)">
      <text class="year-num" x="846" y="152">21</text><text class="year-num" x="846" y="162.5">22</text><text class="year-num" x="846" y="173">23</text><text class="year-num" x="846" y="183.6">24</text><text class="year-num" x="846" y="194.1">25</text><text class="year-num" x="846" y="204.6">26</text><text class="year-num" x="846" y="215.1">27</text><text class="year-num" x="846" y="225.7">28</text><text class="year-num" x="846" y="236.2">29</text><text class="year-num year-num--major" x="846" y="249">30</text>
    </g>
    <g transform="translate(0 362.4)">
      <text class="year-num" x="846" y="152">31</text><text class="year-num" x="846" y="162.5">32</text><text class="year-num" x="846" y="173">33</text><text class="year-num" x="846" y="183.6">34</text><text class="year-num" x="846" y="194.1">35</text><text class="year-num" x="846" y="204.6">36</text><text class="year-num" x="846" y="215.1">37</text><text class="year-num" x="846" y="225.7">38</text><text class="year-num" x="846" y="236.2">39</text><text class="year-num year-num--major" x="846" y="249">40</text>
    </g>
    <g transform="translate(0 483.2)">
      <text class="year-num" x="846" y="152">41</text><text class="year-num" x="846" y="162.5">42</text><text class="year-num" x="846" y="173">43</text><text class="year-num" x="846" y="183.6">44</text><text class="year-num" x="846" y="194.1">45</text><text class="year-num" x="846" y="204.6">46</text><text class="year-num" x="846" y="215.1">47</text><text class="year-num" x="846" y="225.7">48</text><text class="year-num" x="846" y="236.2">49</text><text class="year-num year-num--major" x="846" y="249">50</text>
    </g>
    <g transform="translate(0 604)">
      <text class="year-num" x="846" y="152">51</text><text class="year-num" x="846" y="162.5">52</text><text class="year-num" x="846" y="173">53</text><text class="year-num" x="846" y="183.6">54</text><text class="year-num" x="846" y="194.1">55</text><text class="year-num" x="846" y="204.6">56</text><text class="year-num" x="846" y="215.1">57</text><text class="year-num" x="846" y="225.7">58</text><text class="year-num" x="846" y="236.2">59</text><text class="year-num year-num--major" x="846" y="249">60</text>
    </g>
    <g transform="translate(0 724.8)">
      <text class="year-num" x="846" y="152">61</text><text class="year-num" x="846" y="162.5">62</text><text class="year-num" x="846" y="173">63</text><text class="year-num" x="846" y="183.6">64</text><text class="year-num" x="846" y="194.1">65</text><text class="year-num" x="846" y="204.6">66</text><text class="year-num" x="846" y="215.1">67</text><text class="year-num" x="846" y="225.7">68</text><text class="year-num" x="846" y="236.2">69</text><text class="year-num year-num--major" x="846" y="249">70</text>
    </g>
    <g transform="translate(0 845.6)">
      <text class="year-num" x="846" y="152">71</text><text class="year-num" x="846" y="162.5">72</text><text class="year-num" x="846" y="173">73</text><text class="year-num" x="846" y="183.6">74</text><text class="year-num" x="846" y="194.1">75</text><text class="year-num" x="846" y="204.6">76</text><text class="year-num" x="846" y="215.1">77</text><text class="year-num" x="846" y="225.7">78</text><text class="year-num" x="846" y="236.2">79</text><text class="year-num year-num--major" x="846" y="249">80</text>
    </g>
  </g>

  <text class="axis-title" transform="translate(866 588) rotate(90)">YEAR</text>

  <text class="quote" x="470" y="1112">“Life can only be understood backwards; but it must be lived forwards.”</text>
  <text class="quote-author" x="470" y="1132">HENRIK VASTMOE</text>

  <rect class="brand-band" x="0" y="1150" width="940" height="23"/>
  <text class="brand-name" x="102" y="1167">OLVENTRA</text>
</svg>
</body>
</html>
```